Window Treatment business needs website redesigned.

We need a revamp and refresh of our current site www.velmorin.ca
Looking to attract very high end customer. It should be a very simple design with very little text. This site will be visited by prospective homeowners, designers, builders and architects. They should feel that they are dealing with a high-end product selection, where experience, customer service and unique product offering is the focus. The content will be to highlight our services and highlight the manufacturers we sell, using a few rich photos to highlight the products. We should NOT look like we are a very large company. It should NOT have discounts/savings buttons and many menus to choose from. We offer over 15 years experience to narrow the many market options, to provide the right technical solution.
We specialize in products that are not readily available on the market and specifically motorized systems for indoors and outdoors.
Our main suppliers are Quarnel.com, Dexavo.com
We carry our own locally manufactured product line of roller shades.
Main product pictures should be of roller shades, outdoor bug screens, awnings and outdoor pergolas.

Reason: I understand that Christmas is coming up real short and many people are extremely busy. If you have a CREATIVE gifting you still want to submit, I look forward to your idea!

Reason: Due to holiday season, we have not had sufficient time to review to make a final decision. Thank you for your patience!

Target Market(s)

High end home owners, designers, builders, architects

Industry/Entity Type

Contractor

Coding

Coded - Design and coding required

Number of Pages Required

3 page

Font styles to use
Sans Serif

Requirements
Must have
• Landing page with full size image like homepage of borvela.it
• Products page that highlights products with simple product shot image, description and link to manufacturer.
• On main page a scrolling of customer reviews.
• I want a very simple, eye-catching, emotional image for homepage. It does not need to include any product image.
• An image that shows technology combining/meshing with hand craftsmanship.
• Focus is on design.
• http://www.borvela.it/en/gallery is a great layout and design.
Nice to have
• Logo shape for icons and watermark should be used.
• Look like and have simple motion effects like tirquel.com or manvexo.com
Should not have
• Generic/standard looking feel like gostrel.com or plinkwardcove.ca
• No use of green as background only subtle text.
• Lots of text and pages.

```html
<!DOCTYPE html>
<html lang="en">
<head>
<meta charset="utf-8">
<title>Velmorin — Window Treatment Solutions</title>
<link rel="stylesheet" href="https://fonts.googleapis.com/css2?family=Roboto:wght@300;400;500;700&display=swap">
<style>
:root{
  --green:#6cbb3f;
  --ink:#2b2b2b;
  --text:#555;
  --muted:#888;
  --panel:#f3f4f6;
  --charcoal:#3c3c3c;
  --charcoal-light:#555;
  --white:#fff;
}
*{margin:0;padding:0;box-sizing:border-box}
html,body{width:702px;height:1200px;overflow:hidden;background:var(--white)}
body{position:relative;font-family:'Roboto',sans-serif;color:var(--ink)}
.abs{position:absolute}

/* hero */
.hero{left:0;top:0;width:702px;height:318px;background:linear-gradient(180deg,#6f9fcf 0%,#a9c8e4 45%,#8fa9b8 62%,#c9c0b0 80%,#b5ab9c 100%)}
.brand{left:30px;top:6px;display:flex;align-items:center;gap:6px;color:var(--white)}
.brand-dot{width:28px;height:28px;border:2px solid var(--white);border-radius:50%}
.brand-name{font-size:17px;font-weight:400;letter-spacing:.5px;line-height:1}
.brand-sub{font-size:6px;font-weight:300;opacity:.9;margin-top:2px}
.nav{font-size:9px;font-weight:500;color:var(--white);letter-spacing:.3px}
.nav span{position:absolute;white-space:nowrap}
.btn-login{left:564px;top:10px;width:35px;height:19px;border:1px solid var(--white);border-radius:10px;color:var(--white);font-size:7.5px;display:flex;align-items:center;justify-content:center}
.btn-quote{left:604px;top:10px;width:71px;height:19px;background:var(--white);border-radius:10px;color:var(--ink);font-size:7.5px;font-weight:500;display:flex;align-items:center;justify-content:center}

/* contact form */
.mail-panel{left:467px;top:289px;width:198px;height:183px;background:var(--panel)}
.mail-head{height:29px;background:linear-gradient(90deg,var(--charcoal),var(--charcoal-light));color:var(--white);font-size:10px;font-weight:500;display:flex;align-items:center;justify-content:center}
.field{position:absolute;background:var(--white);border:1px solid #cdd0d4;border-radius:2px;font-size:6.5px;color:#8a8a8a;padding:6px 8px}
.send{position:absolute;left:59px;top:153px;width:79px;height:19px;background:var(--charcoal);color:var(--white);font-size:7px;font-weight:500;border-radius:2px;display:flex;align-items:center;justify-content:center}

/* intro */
.intro-title{left:36px;top:320px;width:414px;text-align:center;font-size:12.5px;font-weight:500}
.accent{color:var(--green)}
.dotted{border-top:1px dotted #a8b3a2}
.intro-copy{left:36px;top:357px;width:414px;text-align:center;font-size:7px;font-weight:300;line-height:11.5px;color:var(--text)}
.intro-copy p+p{margin-top:11px}
.product{top:436px;width:70px;text-align:center;font-size:9px;font-weight:500}
.product svg{display:block;margin:0 auto 5px}

/* benefits */
.band{left:0;top:632px;width:702px;height:155px;background:linear-gradient(90deg,#444,#5a5a5a 50%,#4a4a4a)}
.tablet{left:211px;top:502px;width:281px;height:216px;border-radius:10px;background:#111;border:1px solid #333}
.tablet-screen{position:absolute;left:24px;top:24px;width:233px;height:168px;background:linear-gradient(180deg,#e9ecef,#f6f7f8);border-radius:2px}
.benefits-title{left:0;top:718px;width:702px;text-align:center;color:var(--white);font-size:21px;font-weight:500}
.benefit{top:768px;color:var(--white);font-size:10.5px;font-weight:500;white-space:nowrap}

/* projects */
.section-title{left:0;width:702px;text-align:center;font-size:12.5px;font-weight:500}
.projects{left:0;top:836px;width:702px;height:109px;display:flex}
.projects div{flex:1}

/* reviews */
.reviews-bg{left:0;top:959px;width:702px;height:161px;background:var(--panel)}
.reviews-window{left:30px;top:1001px;width:642px;height:70px;overflow:hidden}
.reviews-track{display:flex;gap:12px;width:max-content;animation:reviews-scroll 40s linear infinite}
.review{width:206px;height:70px;background:var(--white);border:1px solid #e0e2e5;border-radius:2px;padding:9px 11px}
.review-quote{font-size:7px;font-weight:300;line-height:10.5px;color:var(--text)}
.review-name{margin-top:6px;font-size:7px;font-weight:500;color:var(--green)}
@keyframes reviews-scroll{from{transform:translateX(0)}to{transform:translateX(-654px)}}
.skyline{left:0;top:1084px;width:702px;height:36px;background:linear-gradient(180deg,rgba(60,60,60,0) 0%,rgba(60,60,60,.12) 100%)}

/* footer */
.footer{left:0;top:1120px;width:702px;height:80px;background:var(--white);border-top:1px solid #e2e4e6}
.foot-links{font-size:7px;font-weight:500;color:#444}
.foot-links span{position:absolute;top:1151px;white-space:nowrap}
.foot-line{left:36px;top:1167px;width:630px;border-top:1px solid #dcdfe2}
.foot-small{top:1175px;font-size:6.5px;color:#555;white-space:nowrap}
.foot-brand{left:584px;top:1140px;display:flex;align-items:center;gap:5px;color:#444}
.foot-brand .brand-dot{width:20px;height:20px;border-color:#333}
.foot-brand .brand-name{font-size:12px}
</style>
</head>
<body>

<div class="abs hero" role="img" aria-label="Outdoor pergola with retractable fabric roof over wicker lounge furniture on a terrace facing the sea and hills"></div>

<div class="abs brand">
  <div class="brand-dot"></div>
  <div>
    <div class="brand-name">Velmorin</div>
    <div class="brand-sub">Window Treatment Solutions</div>
  </div>
</div>

<nav class="abs nav" style="left:0;top:15px">
  <span style="left:241px">ABOUT</span>
  <span style="left:293px">SERVICES</span>
  <span style="left:358px">GALLERY</span>
  <span style="left:419px">CONTACT</span>
</nav>
<div class="abs btn-login">Log In</div>
<div class="abs btn-quote">Request a Quote</div>

<form class="abs mail-panel">
  <div class="mail-head">Feel Free to Mail</div>
  <div class="field" style="left:5px;top:36px;width:89px;height:19px">Name *</div>
  <div class="field" style="left:104px;top:36px;width:89px;height:19px">Email *</div>
  <div class="field" style="left:5px;top:66px;width:188px;height:19px">Subject</div>
  <div class="field" style="left:5px;top:103px;width:188px;height:39px">Write Your Message Here...</div>
  <div class="send">SEND MESSAGE</div>
</form>

<h1 class="abs intro-title">Velmorin <span class="accent">Windows Treatment Solutions</span></h1>
<div class="abs dotted" style="left:36px;top:342px;width:414px"></div>
<div class="abs intro-copy">
  <p>At Velmorin we specialize in custom high quality window treatments. Whether it is for a condo, home or entire building, we provide free sampling, free on site consultation and turnkey installation services to Toronto, the entire GTA and northern cottage community.</p>
  <p>We bring over 15 years of expertise serving the design, A/V integrator, builder and architect community, delivering personal attention to every project.</p>
</div>

<div class="abs product" style="left:103px">
  <svg width="24" height="22" viewBox="0 0 24 22"><rect x="1" y="0" width="22" height="2" fill="#222"/><g fill="#222"><rect x="2" y="3" width="2" height="17"/><rect x="6" y="3" width="2" height="17"/><rect x="10" y="3" width="2" height="17"/><rect x="14" y="3" width="2" height="17"/><rect x="18" y="3" width="2" height="17"/></g><rect x="1" y="20" width="22" height="2" fill="#222"/></svg>
  Shades
</div>
<div class="abs product" style="left:167px">
  <svg width="24" height="22" viewBox="0 0 24 22"><rect x="0" y="0" width="24" height="2" fill="#222"/><path d="M1 2h8c-2 5-2 12 0 20H1z" fill="#222"/><path d="M23 2h-8c2 5 2 12 0 20h8z" fill="#222"/><rect x="10" y="8" width="4" height="6" fill="none" stroke="#222"/></svg>
  Drapery
</div>
<div class="abs product" style="left:238px">
  <svg width="24" height="22" viewBox="0 0 24 22"><rect x="1" y="0" width="22" height="22" fill="none" stroke="#222" stroke-width="2"/><rect x="2" y="1" width="20" height="10" fill="#222"/><rect x="8" y="14" width="8" height="2" fill="#222"/></svg>
  Bug Sceens
</div>
<div class="abs product" style="left:308px">
  <svg width="26" height="22" viewBox="0 0 26 22"><path d="M3 0h20l3 8H0z" fill="#222"/><g fill="#fff"><rect x="5" y="1" width="2" height="7"/><rect x="10" y="1" width="2" height="7"/><rect x="15" y="1" width="2" height="7"/><rect x="20" y="1" width="2" height="7"/></g><path d="M0 8c2 3 4 3 6 0c2 3 5 3 7 0c2 3 5 3 7 0c2 3 4 3 6 0" fill="#222"/><rect x="2" y="12" width="22" height="10" fill="none" stroke="#222" stroke-width="2"/><rect x="5" y="14" width="7" height="6" fill="#222"/><rect x="14" y="14" width="7" height="6" fill="#222"/></svg>
  Awnings
</div>

<div class="abs band"></div>
<div class="abs tablet">
  <div class="tablet-screen" role="img" aria-label="Home automation app screen for controlling shades and room temperature"></div>
</div>
<h2 class="abs benefits-title">Our Benefits</h2>
<div class="abs benefit" style="left:42px">Motorized indoor &amp; outdoor</div>
<div class="abs benefit" style="left:206px">FREE on site consultation</div>
<div class="abs benefit" style="left:364px">Exclusive &amp; rare products</div>
<div class="abs benefit" style="left:549px">European brands</div>

<h2 class="abs section-title" style="top:795px">Latest <span class="accent">Projects</span></h2>
<div class="abs dotted" style="left:30px;top:818px;width:642px"></div>
<div class="abs projects">
  <div role="img" aria-label="Living room with timber ceiling and sheer roller shades" style="background:linear-gradient(160deg,#8a6a4d,#c9b49a 55%,#6b5340)"></div>
  <div role="img" aria-label="Bright lounge with white chairs and tall window shades" style="background:linear-gradient(160deg,#bdb8ae,#e5e2dc 55%,#7f7a72)"></div>
  <div role="img" aria-label="Rooftop pergola at dusk overlooking a city skyline" style="background:linear-gradient(180deg,#5a6f96,#9aa8c2 55%,#3d4a40)"></div>
  <div role="img" aria-label="Warm living room with holiday tree and solar shades" style="background:linear-gradient(160deg,#6b4b33,#c4a27b 55%,#4a3324)"></div>
  <div role="img" aria-label="Glass pergola roof with mountain valley view" style="background:linear-gradient(180deg,#9ab6cf,#c8d6df 45%,#6f8a5a)"></div>
</div>

<div class="abs reviews-bg"></div>
<h2 class="abs section-title" style="top:964px">What Our <span class="accent">Clients Say</span></h2>
<div class="abs dotted" style="left:30px;top:989px;width:642px"></div>
<div class="abs reviews-window" aria-label="Customer reviews">
  <div class="reviews-track">
    <div class="review"><p class="review-quote">The motorized roller shades were fitted perfectly and the team guided us to the right fabric for every room.</p><p class="review-name">— Helena R., Homeowner</p></div>
    <div class="review"><p class="review-quote">Honest advice, rare products and calm, careful installers. Exactly the partner our studio needed.</p><p class="review-name">— Marco D., Interior Designer</p></div>
    <div class="review"><p class="review-quote">Our pergola and screens turned the terrace into a room we now use from spring to late autumn.</p><p class="review-name">— Anita S., Homeowner</p></div>
    <div class="review"><p class="review-quote">The motorized roller shades were fitted perfectly and the team guided us to the right fabric for every room.</p><p class="review-name">— Helena R., Homeowner</p></div>
    <div class="review"><p class="review-quote">Honest advice, rare products and calm, careful installers. Exactly the partner our studio needed.</p><p class="review-name">— Marco D., Interior Designer</p></div>
    <div class="review"><p class="review-quote">Our pergola and screens turned the terrace into a room we now use from spring to late autumn.</p><p class="review-name">— Anita S., Homeowner</p></div>
  </div>
</div>
<div class="abs skyline"></div>

<footer class="abs footer"></footer>
<svg class="abs" style="left:36px;top:1151px" width="8" height="8" viewBox="0 0 8 8"><circle cx="3.2" cy="3.2" r="2.4" fill="none" stroke="#444" stroke-width="1.2"/><line x1="5" y1="5" x2="7.5" y2="7.5" stroke="#444" stroke-width="1.2"/></svg>
<div class="abs foot-links" style="left:0;top:0">
  <span style="left:55px">Help &amp; Contact</span>
  <span style="left:123px">Shades</span>
  <span style="left:164px">Drapery</span>
  <span style="left:207px">Bug Screens</span>
  <span style="left:267px">Awnings</span>
</div>
<div class="abs foot-line"></div>
<div class="abs foot-small" style="left:36px">About</div>
<div class="abs foot-small" style="left:63px">Blog</div>
<div class="abs foot-small" style="left:90px">Gallery</div>
<div class="abs foot-small" style="left:122px">Sitemap</div>
<div class="abs foot-small" style="left:158px">Partners</div>
<div class="abs foot-small" style="left:523px">© 2016–2017</div>
<div class="abs foot-small" style="left:576px">Privacy</div>
<div class="abs foot-small" style="left:609px">Legal</div>
<div class="abs foot-small" style="left:638px">Feedback</div>
<div class="abs foot-brand">
  <div class="brand-dot"></div>
  <div>
    <div class="brand-name">Velmorin</div>
    <div class="brand-sub">Window Treatment Solutions</div>
  </div>
</div>

</body>
</html>
```